Website design for a construction company

The logo and the copies of all the 3 pages are attached below. I don't have a preference in colors but I would ideally like to use the colors on my logo, dark teal (secondary) and copper (primary).

Company Name: Torvin Group

Location: London, UK

Business Overview:

Torvin Group is a comprehensive construction company based in London, specializing in a wide range of construction services. We cater to various sectors, providing services including electrical work, painting and decorating, plastering, plumbing, carpentry, kitchen and bathroom installations, loft conversions, and extensions. Our team is known for its skilled craftsmanship, attention to detail, and commitment to quality.

What "TORVIN" stands for:

Our company name, 'TORVIN', is derived from Hephaestus, the ancient Greek god of craftsmen, blacksmiths, artisans, sculptors, metals, metallurgy, fire, and volcanoes. Hephaestus was renowned in mythology for his incredible skill in crafting and creating, making him the patron of all craftsmen and artisans. His name is synonymous with the mastery of artisanship and the creation of wondrous, enduring works.

In choosing 'TORVIN' as our name, we embody the spirit and skills of Hephaestus. It reflects our commitment to craftsmanship, excellence, and durability in the field of construction. Just as Hephaestus was known for his meticulous work, precision, and innovative creations, our company strives to uphold these qualities in every project we undertake.

Our name is a constant reminder of our dedication to quality, innovation, and the art of building. It symbolizes our endeavor to achieve the highest standards in construction, much like Hephaestus did in his timeless creations. In essence, 'TORVIN' is not just our name; it's a representation of our ethos and the high standards we set for ourselves in the construction industry.

Target Audience:

Our primary audience includes homeowners, real estate developers, and commercial clients in London seeking reliable, high-quality construction services.

Unique Selling Points:

Diverse Range of Services: Offering a one-stop solution for all construction needs.

Certified and Experienced: Professional team with a strong focus on delivering certified and compliant work, particularly in electrical services.

Client-Centric Approach: Emphasizing client satisfaction, we tailor our services to meet the unique needs and visions of our clients.

Quality and Reliability: Commitment to high-quality materials, skilled workmanship, and delivering projects on time and within budget.

Website Requirements:

Clean, professional design reflecting the quality and reliability of our services.

User-friendly navigation to easily access information about our services, portfolio, company background, and contact details.

Portfolio section showcasing our past projects with placeholders for images and descriptions.

Integration of a contact form, map for our location, and links to our social media accounts.

Mobile-responsive design to ensure accessibility across various devices.

Purpose of the Website:
The website aims to:

Establish an online presence and credibility in the construction industry.

Provide an informative resource about our services and past projects to potential clients.

Facilitate easy communication and inquiries through an integrated contact system.

Tone and Style:

Professional, informative, and welcoming. The website should convey trustworthiness and expertise in the construction field.

homeowners, real estate developers, and commercial clients

Construction

3 page

```html
<!DOCTYPE html>
<html lang="en">
<head>
<meta charset="utf-8">
<title>About Us – Torvin Group</title>
<link href="https://fonts.googleapis.com/css2?family=Questrial&family=Inter:wght@400;500;600&display=swap" rel="stylesheet">
<style>
:root{
  --teal:#0b4d4a;
  --copper:#b87333;
  --sky:#7aacd6;
  --line:#c9d6d5;
  --ink:#111;
  --white:#fff;
}
*{box-sizing:border-box;margin:0;padding:0}
html,body{width:1200px;height:3368px;overflow:hidden;background:var(--white)}
body{position:relative;font-family:"Inter",sans-serif;color:var(--teal)}
.abs{position:absolute}
.heading{font-family:"Questrial",sans-serif;font-weight:400;letter-spacing:-0.02em}
a{color:inherit;text-decoration:none}

/* brand */
.brand{display:flex;align-items:center;gap:8px}
.brand-mark{width:26px;height:26px;background:var(--copper)}
.brand-name{font-family:"Inter",sans-serif;font-weight:500;font-size:28px;color:var(--teal);letter-spacing:-0.01em}

/* top bar */
.topbar{left:0;top:0;width:1200px;height:97px;border-bottom:1px solid var(--line)}
.topbar .brand{position:absolute;left:95px;top:38px}
.contact-row{display:flex;align-items:center;gap:10px;font-size:11.5px;font-weight:600;color:var(--teal)}
.contact-row .item{display:flex;align-items:center;gap:10px;margin-left:22px}
.topbar .contact-row{position:absolute;right:94px;top:49px}
.icon{width:15px;height:15px;stroke:var(--teal);fill:none;stroke-width:1.6}

/* nav */
.nav{left:0;top:97px;width:1200px;height:75px;border-bottom:1px solid var(--line)}
.nav ul{list-style:none;display:flex;gap:39px;position:absolute;left:93px;top:31px;font-size:12px;font-weight:500}
.nav .active{font-weight:600;text-decoration:underline;text-underline-offset:3px}
.btn-register{position:absolute;left:945px;top:19px;width:161px;height:36px;background:var(--copper);color:var(--white);border-radius:4px;font-size:13px;font-weight:500;display:flex;align-items:center;justify-content:center;gap:10px}

/* hero */
.hero-title{left:93px;top:308px;font-size:76px;line-height:72px}
.hero-title .lead{color:var(--copper);display:inline-block;border-bottom:2px solid var(--copper);line-height:66px}
.hero-title .sub{color:var(--teal)}
.hero-tagline{left:93px;top:481px;font-size:20px;letter-spacing:0.01em}
.hero-portrait{left:833px;top:275px;width:261px;height:281px;background:linear-gradient(180deg,#f2f0ee 0%,#cfc8c2 40%,#3e4a30 75%,#2f3a26 100%)}

/* accordion */
.band{left:20px;width:1160px;height:71px;background:var(--copper);color:var(--white);font-family:"Questrial",sans-serif;font-size:23px;letter-spacing:-0.01em;display:flex;align-items:center;padding-left:73px}
.band .toggle{position:absolute;right:82px;top:34px;width:24px;height:2px;background:var(--white)}
.panel{left:20px;width:1160px;border:1px solid var(--line);border-top:none}
.panel h2{position:absolute;left:73px;font-size:51px;color:var(--teal)}
.panel p{position:absolute;left:73px;width:920px;font-size:16px;line-height:20px;color:var(--teal)}
.chev{position:absolute;right:80px;width:24px;height:14px;stroke:var(--teal);fill:none;stroke-width:1.6}

/* team */
.team-title{left:73px;top:1765px;font-size:76px;color:var(--ink)}
.team-quote{left:73px;top:1864px;width:1020px;font-size:20px;line-height:27px;color:var(--teal)}
.card{left:73px;width:1053px;height:182px;border:1px solid #dcdcdc;border-radius:8px}
.card.accent{background:var(--copper);border-color:var(--copper);color:var(--white)}
.card .media{position:absolute;top:20px;width:497px;height:142px;border-radius:6px}
.card h3{position:absolute;font-size:38px;color:var(--ink);font-family:"Questrial",sans-serif;font-weight:400;letter-spacing:-0.02em}
.card.accent h3{color:var(--white)}
.card p{position:absolute;width:500px;font-size:12.5px;line-height:18.5px;color:var(--teal)}
.card.accent p{color:var(--white)}

/* vision */
.vision{left:20px;top:2650px;width:1160px;height:350px;background:var(--sky);color:var(--white);text-align:center}
.vision h2{position:absolute;left:0;right:0;top:70px;font-size:76px}
.vision p{position:absolute;left:70px;right:70px;top:178px;font-size:20px;line-height:27px}

/* footer */
.footer .brand{position:absolute;left:60px;top:3054px}
.footer-about{left:60px;top:3124px;width:470px;font-size:16px;line-height:27px}
.footer-links{left:720px;top:3123px;display:grid;grid-template-columns:147px 147px 100px;row-gap:20px;font-size:16px;list-style:none}
.socials{left:62px;top:3225px;display:flex;gap:16px}
.socials span{width:16px;height:16px;border:1.6px solid var(--teal);border-radius:50%}
.footer .contact-row{position:absolute;left:60px;top:3262px;font-size:11.5px}
.footer .contact-row .item:first-child{margin-left:0}
.legal{left:0;top:3318px;width:1200px;border-top:1px solid var(--line);height:50px;font-size:11.5px;font-weight:500}
.legal .copy{position:absolute;left:60px;top:15px}
.legal .policy{position:absolute;right:62px;top:15px;display:flex;gap:22px}
</style>
</head>
<body>

<header class="topbar abs">
  <div class="brand"><span class="brand-mark"></span><span class="brand-name">TORVIN</span></div>
  <div class="contact-row">
    <span class="item"><svg class="icon" viewBox="0 0 16 16"><rect x="2" y="3.5" width="12" height="9" rx="1"/><path d="M2 4.5l6 4.5 6-4.5"/></svg>torvin****@mailbox.co</span>
    <span class="item"><svg class="icon" viewBox="0 0 16 16"><path d="M3 2.5h3l1.2 3-1.7 1.2a8 8 0 0 0 3.8 3.8l1.2-1.7 3 1.2v3a1 1 0 0 1-1 1A11 11 0 0 1 2 3.5a1 1 0 0 1 1-1z"/></svg>+44 20 *******</span>
    <span class="item"><svg class="icon" viewBox="0 0 16 16"><path d="M8 14.5s-4.5-4.3-4.5-7.8a4.5 4.5 0 0 1 9 0c0 3.5-4.5 7.8-4.5 7.8z"/><circle cx="8" cy="6.7" r="1.6"/></svg>London, UK</span>
  </div>
</header>

<nav class="nav abs">
  <ul>
    <li><a href="#">Home</a></li>
    <li><a href="#" class="active">About Us</a></li>
    <li><a href="#">Our Service</a></li>
    <li><a href="#">Portfolio</a></li>
    <li><a href="#">Contact</a></li>
  </ul>
  <a href="#" class="btn-register">Register Now
    <svg width="10" height="10" viewBox="0 0 10 10" fill="none" stroke="#fff" stroke-width="1.5"><path d="M2 8l6-6M3.5 2H8v4.5"/></svg>
  </a>
</nav>

<section class="hero">
  <h1 class="hero-title heading abs"><span class="lead">Our Story,</span><br><span class="sub">Your Confidence</span></h1>
  <p class="hero-tagline abs">Pioneering Construction Excellence in London</p>
  <div class="hero-portrait abs" role="img" aria-label="Portrait of the company founder in a dark green polo shirt"></div>
</section>

<section class="journey">
  <div class="band abs" style="top:650px">OUR JOURNEY<span class="toggle"></span></div>
  <div class="panel abs" style="top:721px;height:224px">
    <h2 class="heading" style="top:48px">Introduction</h2>
    <p style="top:123px">At Torvin Group, our journey began with a vision – to create a construction company that stands apart in its commitment to excellence, reliability, and customer satisfaction. Based in the heart of London, we've grown from a small team of enthusiastic builders to a full-fledged construction company renowned for quality and integrity</p>
    <svg class="chev" style="top:104px" viewBox="0 0 24 14"><path d="M2 12L12 2l10 10"/></svg>
  </div>
  <div class="panel abs" style="top:945px;height:243px">
    <h2 class="heading" style="top:48px">History</h2>
    <p style="top:125px">Founded in 2024, by Aren Voskuil and Milo Dretham, our company has a rich history of overcoming challenges and embracing innovation. With each project, we've not only built structures but also strong relationships with our clients and community.</p>
    <svg class="chev" style="top:104px" viewBox="0 0 24 14"><path d="M2 12L12 2l10 10"/></svg>
  </div>
</section>

<section class="philosophy">
  <div class="band abs" style="top:1188px">OUR PHILOSOPHY<span class="toggle"></span></div>
  <div class="panel abs" style="top:1259px;height:265px">
    <h2 class="heading" style="top:50px">Core Values</h2>
    <p style="top:133px;line-height:26.5px">Our core values are the pillars of our success. Integrity, quality, and customer focus drive us to exceed expectations on every project. We believe in transparent communication, ethical practices, and a commitment to delivering the best possible outcome for our clients.</p>
    <svg class="chev" style="top:126px" viewBox="0 0 24 14"><path d="M2 12L12 2l10 10"/></svg>
  </div>
  <div class="panel abs" style="top:1524px;height:166px">
    <h2 class="heading" style="top:52px">Approach to Construction:</h2>
    <svg class="chev" style="top:76px" viewBox="0 0 24 14"><path d="M2 2l10 10L22 2"/></svg>
  </div>
</section>

<section class="team">
  <h2 class="team-title heading abs">Our Team</h2>
  <p class="team-quote abs">“Lorem Ipsum is simply dummy text of the printing and typesetting industry. Lorem Ipsum has been the industry's standard dummy text ever since the 1500s”</p>

  <article class="card abs" style="top:1969px">
    <div class="media" style="left:20px;background:linear-gradient(120deg,#8e9498,#5a5350 45%,#c0653a 60%,#8a8f93)" role="img" aria-label="Construction worker in a hard hat and hi-vis vest on scaffolding"></div>
    <h3 style="left:537px;top:14px">Expertise</h3>
    <p style="left:537px;top:70px">Our team is our greatest asset. Comprising experienced professionals from various construction disciplines, we bring a wealth of knowledge and skill to every project. Our electricians, painters, decorators, plumbers, carpenters, and other specialists are not just experts in their fields; they are also committed to our ethos of excellence</p>
  </article>

  <article class="card accent abs" style="top:2172px">
    <h3 style="left:20px;top:34px">Training and Development:</h3>
    <p style="left:20px;top:94px;width:500px">Continual training and development are key to our success. We invest in our team's growth, ensuring they stay at the forefront of industry advancements and safety standards.</p>
    <div class="media" style="left:536px;background:linear-gradient(180deg,#6f6a60,#8a8577 45%,#d9d7d2 75%,#f0efec)" role="img" aria-label="Site crew in hi-vis vests inspecting a rebar grid on a large foundation"></div>
  </article>

  <article class="card abs" style="top:2374px">
    <div class="media" style="left:20px;background:linear-gradient(120deg,#1d1f22,#4a4a48 50%,#d8d3c8 70%,#2a2c2e)" role="img" aria-label="Hands drafting building plans on paper with a ruler and pencil"></div>
    <h3 style="left:537px;top:24px">Sustainable Practices:</h3>
    <p style="left:537px;top:80px">Sustainability is integral to our operations. We strive to minimize our environmental impact through efficient use of resources, waste reduction, and environmentally friendly materials. Our goal is to create not just aesthetically pleasing spaces but also sustainable ones that respect our planet</p>
  </article>
</section>

<section class="vision abs">
  <h2 class="heading">Vision for the Future</h2>
  <p>”As we look to the future, our aim is to continue being a leader in London's construction industry, pushing boundaries, and setting new standards. We're excited about the opportunities to innovate, grow, and contribute to our community's development.”</p>
</section>

<footer class="footer">
  <div class="brand"><span class="brand-mark"></span><span class="brand-name">TORVIN</span></div>
  <p class="footer-about abs">Where Construction Meets Excellence.&nbsp; Based in London, we are committed to transforming your spaces into exceptional places.</p>
  <ul class="footer-links abs">
    <li><a href="#">Home</a></li><li><a href="#">Project</a></li><li><a href="#">Service</a></li>
    <li><a href="#">About Us</a></li><li><a href="#">Contact Us</a></li><li><a href="#">FAQ</a></li>
  </ul>
  <div class="socials abs" aria-label="Social media links"><span></span><span></span><span></span><span></span></div>
  <div class="contact-row">
    <span class="item"><svg class="icon" viewBox="0 0 16 16"><rect x="2" y="3.5" width="12" height="9" rx="1"/><path d="M2 4.5l6 4.5 6-4.5"/></svg>torvin****@mailbox.co</span>
    <span class="item"><svg class="icon" viewBox="0 0 16 16"><path d="M3 2.5h3l1.2 3-1.7 1.2a8 8 0 0 0 3.8 3.8l1.2-1.7 3 1.2v3a1 1 0 0 1-1 1A11 11 0 0 1 2 3.5a1 1 0 0 1 1-1z"/></svg>+44 20 *******</span>
    <span class="item"><svg class="icon" viewBox="0 0 16 16"><path d="M8 14.5s-4.5-4.3-4.5-7.8a4.5 4.5 0 0 1 9 0c0 3.5-4.5 7.8-4.5 7.8z"/><circle cx="8" cy="6.7" r="1.6"/></svg>London, UK</span>
  </div>
  <div class="legal abs">
    <span class="copy">Torvin Group, Inc. © 2024 All Rights Reserved.</span>
    <span class="policy"><a href="#">Privacy &amp; Policy</a><a href="#">Terms &amp; Conditions</a></span>
  </div>
</footer>

</body>
</html>
```